3D Printing Business coming soon page

Hi we are looking for a one page "coming soon" website for our business. The business is called "Strideform Labs" and it is a new solution which 3D Prints Orthotics (Insoles).

The design should include our logo, an improved version of our promotional image (attached), a web form for capturing interest from people, a countdown timer and some text.

Follow the colour scheme which is shown in our logo along with our other colours - Orange (RGB#ff8300) and Light Green (RGB#30f20a)
Updates

Industry/Entity Type

Business

Font styles to use
Sans Serif

Requirements
Must have
• Logo (Attached)
Improved version of Promotional Image
Web Form design for capturing Name, EMail Address and Comments along with a Turin test
Countdown Timer
Text - "Strideform Labs will shake up the Orthotics Industry. Foot Orthosis patient-ready in hours for a fraction of the price you are paying today. Welcome to the new world of 3D Printing!"

Files

```html
<!DOCTYPE html>
<html lang="en">
<head>
<meta charset="utf-8">
<title>Strideform Labs — Coming Soon</title>
<link href="https://fonts.googleapis.com/css2?family=Lato:ital,wght@0,300;0,400;0,700;0,900;1,400;1,700&family=Lily+Script+One&display=swap" rel="stylesheet">
<style>
  :root {
    --bg: #f9fbfb;
    --blue: #1375a3;
    --blue-deep: #0d6a92;
    --pink: #e03a72;
    --grey-text: #5a5a5a;
    --grey-soft: #9a9a9a;
    --track: #d6d6d6;
    --field: #e9eff5;
    --field-border: #c9d7e4;
    --focus: #f2a27b;
    --footer: #2b2b2b;
    --footer-text: #b8b8b8;
  }
  * { box-sizing: border-box; margin: 0; padding: 0; }
  html, body { width: 1010px; height: 1200px; overflow: hidden; }
  body { position: relative; background: var(--bg); font-family: "Lato", sans-serif; color: var(--grey-text); }
  .abs { position: absolute; }

  .brand { left: 160px; top: 140px; width: 200px; display: flex; align-items: center; gap: 10px; }
  .brand-dot { width: 34px; height: 34px; border-radius: 50%; background: var(--blue); flex: none; }
  .brand-name { font-weight: 900; font-size: 24px; line-height: 1.05; color: var(--blue); }

  .headline { left: 386px; top: 54px; width: 460px; font-weight: 900; font-size: 29px; line-height: 1.2; color: var(--blue); letter-spacing: -0.3px; }
  .headline em { font-style: normal; color: var(--pink); }
  .lead { left: 386px; top: 166px; width: 480px; font-weight: 300; font-size: 19px; line-height: 1.45; color: var(--grey-text); }
  .welcome { left: 389px; top: 249px; font-weight: 300; font-size: 19px; color: var(--grey-text); }
  .welcome strong { font-weight: 700; font-style: italic; }

  .divider { left: 126px; width: 758px; height: 84px; }

  .section-title { left: 0; width: 1010px; text-align: center; font-weight: 400; font-size: 26px; color: var(--pink); letter-spacing: 0.5px; }
  .section-sub { left: 0; width: 1010px; text-align: center; font-style: italic; font-size: 13.5px; color: var(--grey-text); }

  .track { left: 126px; top: 458px; width: 758px; height: 7px; border-radius: 4px; background: var(--track); }
  .step-num { width: 48px; height: 48px; top: 438px; border-radius: 50%; background: #d4d6d8; display: flex; align-items: center; justify-content: center; }
  .step-num span { width: 34px; height: 34px; border-radius: 50%; background: radial-gradient(circle at 40% 30%, #3aa4d4, var(--blue-deep)); color: #fff; font-weight: 900; font-size: 20px; display: flex; align-items: center; justify-content: center; }
  .step-label { top: 499px; width: 190px; text-align: center; font-weight: 700; font-size: 15px; color: var(--blue); }
  .step-photo { top: 536px; width: 172px; height: 172px; border-radius: 50%; border: 2px solid #dcdcdc; background: #fff; box-shadow: 0 1px 4px rgba(0,0,0,.12); padding: 8px; }
  .step-photo div { width: 100%; height: 100%; border-radius: 50%; }

  .coming { left: 150px; top: 906px; width: 200px; text-align: center; font-style: italic; font-weight: 700; font-size: 25px; color: var(--grey-soft); }
  .count-box { top: 958px; width: 57px; height: 61px; border-radius: 4px; background: linear-gradient(#1680b0 50%, #0f6f9c 50%); box-shadow: 0 2px 3px rgba(0,0,0,.2); color: #fff; font-family: "Lily Script One", "Lato", sans-serif; font-size: 28px; display: flex; align-items: center; justify-content: center; }
  .count-label { top: 1028px; width: 57px; text-align: center; font-size: 9px; color: var(--grey-text); letter-spacing: 0.3px; }

  .field { background: var(--field); border: 2px solid var(--field-border); border-radius: 3px; font-size: 10px; color: #555; padding: 0 14px; display: flex; align-items: center; justify-content: space-between; }
  .field.is-focus { border-color: var(--focus); }
  .field.is-area { align-items: flex-start; padding-top: 12px; }
  .captcha { left: 638px; top: 958px; width: 236px; height: 98px; border: 1px solid #dde3e8; border-radius: 3px; background: #fff; }
  .captcha-art { position: absolute; left: 30px; top: 10px; width: 176px; height: 50px; background: linear-gradient(90deg, #f1f1f1, #e4e4e4); border-radius: 2px; }
  .captcha-row { position: absolute; left: 0; bottom: 0; width: 100%; height: 30px; border-top: 1px solid #e4e8eb; display: flex; font-size: 10px; font-weight: 700; color: #555; }
  .captcha-row .hint { flex: 1; padding-left: 13px; display: flex; align-items: center; }
  .captcha-row .tool { width: 30px; border-left: 1px solid #e4e8eb; display: flex; align-items: center; justify-content: center; }

  .submit { left: 765px; top: 1071px; width: 110px; height: 36px; border-radius: 3px; border: 1px solid #c93a69; background: linear-gradient(#f07fa3, #e25885); color: #fff; font-weight: 700; font-size: 14px; display: flex; align-items: center; justify-content: center; }

  .footer { left: 0; top: 1153px; width: 1010px; height: 47px; background: var(--footer); }
  .footer-copy { left: 136px; top: 16px; font-size: 9.5px; color: var(--footer-text); }
  .footer-share { left: 646px; top: 18px; font-size: 9.5px; color: var(--footer-text); }
  .social { top: 9px; width: 26px; height: 26px; border-radius: 2px; }
</style>
</head>
<body>

<header>
  <div class="abs brand"><span class="brand-dot"></span><span class="brand-name">Strideform Labs</span></div>
  <h1 class="abs headline">Strideform Labs will <em>shake up</em> the Orthotics Industry.</h1>
  <p class="abs lead">Foot Orthosis patient-ready in hours for a fraction of the price you are paying today.</p>
  <p class="abs welcome">Welcome to the new world of <strong>3D Printing!</strong></p>
</header>

<svg class="abs divider" style="top:280px" viewBox="0 0 758 84" aria-hidden="true">
  <defs><linearGradient id="shade" x1="0" y1="0" x2="0" y2="1"><stop offset="0" stop-color="#e6e9ea"/><stop offset="1" stop-color="#f9fbfb" stop-opacity="0"/></linearGradient></defs>
  <path d="M0 25 L379 51 L758 25 L758 70 L0 70 Z" fill="url(#shade)"/>
  <path d="M0 25 L379 51 L758 25" fill="none" stroke="#dfe2e3" stroke-width="1"/>
</svg>

<section class="how">
  <h2 class="abs section-title" style="top:366px">HOW IT WORKS?</h2>
  <p class="abs section-sub" style="top:401px">in 4 easy steps!</p>
  <div class="abs track"></div>
  <div class="abs step-num" style="left:197px"><span>1</span></div>
  <div class="abs step-num" style="left:386px"><span>2</span></div>
  <div class="abs step-num" style="left:575px"><span>3</span></div>
  <div class="abs step-num" style="left:765px"><span>4</span></div>
  <p class="abs step-label" style="left:126px">Scan your Feet</p>
  <p class="abs step-label" style="left:315px">Design the Orthodic</p>
  <p class="abs step-label" style="left:504px">Print it in 3D</p>
  <p class="abs step-label" style="left:694px">Fit it!</p>
  <div class="abs step-photo" style="left:135px"><div role="img" aria-label="Tablet with a foot scanner attached" style="background:radial-gradient(circle,#d9dadb,#f4f4f4 75%)"></div></div>
  <div class="abs step-photo" style="left:324px"><div role="img" aria-label="Desktop monitor showing orthotic design software" style="background:radial-gradient(circle,#e8e3e0 30%,#cfd2d4 55%,#f6f6f6 75%)"></div></div>
  <div class="abs step-photo" style="left:513px"><div role="img" aria-label="3D printer with blue interior and red top" style="background:radial-gradient(circle,#8fc6dc 25%,#c7c9c9 50%,#f4f4f4 75%)"></div></div>
  <div class="abs step-photo" style="left:702px"><div role="img" aria-label="Hand placing a printed insole into a shoe" style="background:radial-gradient(circle at 50% 45%,#d9c6a4 25%,#4a4a4a 55%,#f1f1f1 78%)"></div></div>
</section>

<svg class="abs divider" style="top:744px" viewBox="0 0 758 84" aria-hidden="true">
  <path d="M0 25 L379 51 L758 25 L758 70 L0 70 Z" fill="url(#shade)"/>
  <path d="M0 25 L379 51 L758 25" fill="none" stroke="#dfe2e3" stroke-width="1"/>
</svg>

<section class="notify">
  <h2 class="abs section-title" style="top:831px">NOTIFY ME!</h2>
  <p class="abs section-sub" style="top:867px;font-size:14px">Get the latest updates when it comes out!</p>

  <p class="abs coming">Coming soon!</p>
  <div class="abs count-box" style="left:136px">07</div>
  <div class="abs count-box" style="left:223px">23</div>
  <div class="abs count-box" style="left:310px">19</div>
  <p class="abs count-label" style="left:136px">DAYS</p>
  <p class="abs count-label" style="left:223px">HOURS</p>
  <p class="abs count-label" style="left:310px">MINUTES</p>

  <div class="abs field is-focus" style="left:387px;top:912px;width:236px;height:35px">Enter Your Name
    <svg width="12" height="14" viewBox="0 0 12 14" aria-hidden="true"><circle cx="6" cy="4" r="3" fill="#c3c9ce"/><path d="M0 14 Q6 5 12 14Z" fill="#c3c9ce"/></svg></div>
  <div class="abs field" style="left:638px;top:913px;width:236px;height:35px">Your Email
    <svg width="15" height="10" viewBox="0 0 15 10" aria-hidden="true"><rect x="0.5" y="0.5" width="14" height="9" fill="#d0d6dc" stroke="#c0c7cd"/><path d="M0.5 0.5 L7.5 6 L14.5 0.5" fill="none" stroke="#f2f4f6"/></svg></div>
  <div class="abs field is-area" style="left:387px;top:958px;width:236px;height:97px">Your Message
    <svg width="13" height="11" viewBox="0 0 13 11" aria-hidden="true"><ellipse cx="6.5" cy="5" rx="6.5" ry="4.5" fill="#c3c9ce"/><path d="M2 8 L1 11 L5 9Z" fill="#c3c9ce"/></svg></div>

  <div class="abs captcha">
    <div class="captcha-art" role="img" aria-label="Distorted verification code"></div>
    <div class="captcha-row">
      <span class="hint">Type the above code</span>
      <span class="tool"><svg width="11" height="11" viewBox="0 0 12 12" aria-hidden="true"><path d="M10 6 A4 4 0 1 1 8 2.5" fill="none" stroke="#555" stroke-width="1.6"/><path d="M7 0 L10 2.5 L7 4Z" fill="#555"/></svg></span>
      <span class="tool"><svg width="12" height="10" viewBox="0 0 12 10" aria-hidden="true"><path d="M0 3 H3 L6 0 V10 L3 7 H0Z" fill="#555"/><path d="M8 3 Q9.5 5 8 7 M10 1.5 Q12.5 5 10 8.5" fill="none" stroke="#555"/></svg></span>
      <span class="tool"><svg width="11" height="11" viewBox="0 0 12 12" aria-hidden="true"><circle cx="6" cy="6" r="6" fill="#444"/><rect x="5.1" y="2.5" width="1.8" height="4.5" fill="#fff"/><circle cx="6" cy="9" r="1" fill="#fff"/></svg></span>
    </div>
  </div>

  <div class="abs submit">Submit</div>
</section>

<footer class="abs footer">
  <p class="abs footer-copy">Copyright 2014 Strideform Labs |&nbsp; All Rights Reserved &nbsp;|&nbsp; Privacy Policy</p>
  <p class="abs footer-share">Share this!</p>
  <span class="abs social" style="left:706px;background:#3b5a96"></span>
  <span class="abs social" style="left:742px;background:#2fa8de"></span>
  <span class="abs social" style="left:778px;background:#1a6d9b"></span>
  <span class="abs social" style="left:814px;background:#c9242b"></span>
  <span class="abs social" style="left:849px;background:#d7412f"></span>
</footer>

</body>
</html>
```